Strategic Plan Notecards (4.25in x 5.5 in)

I need a design for project cards that will be handed out to the general public as part of a Strategic Planning effort for a client. I'd like the cards to be 4.25 x 5.5 so that they can be printed 4 to a US letter-size sheet of paper.

The Project title is "City of Fieldhaven Strategic Plan Update"
Needs to include text:

For more info, go to www.plainsfutureplan.org
Take the Vision Survey at http://tnyurl.example/FieldhavenIdeas
What do YOU want Fieldhaven to be?

Other variations on this text will be considered.

Target Market(s)

General Public

Font styles to use
Serif
Sans Serif

Colors

Designer to choose colors to be used in the design.

Requirements
Must have
• An interesting and fun visual appeal. Nothing stuffy. Should have a bright graphic background and interesting typefaces for the text.
Nice to have
• One of the biggest assets in the community is the Missouri River - some depiction of a river would be great.

```html
<!DOCTYPE html>
<html lang="en">
<head>
<meta charset="utf-8">
<title>City of Fieldhaven Strategic Plan Update – Notecard</title>
<link rel="stylesheet" href="https://fonts.googleapis.com/css2?family=Fredoka:wght@600&family=Quicksand:wght@700&family=Open+Sans:wght@700&display=swap">
<style>
  :root{
    --backdrop:#c4c4c4;
    --paper:#fbf5e6;
    --halo:#efe4c8;
    --teal:#04838f;
    --teal-light:#4cc4c0;
    --pink:#e0436d;
    --gold:#fccb45;
    --title-gold:#f1b828;
    --ink:#2a2526;
    --navy:#1b3158;
    --white:#ffffff;
  }
  html,body{margin:0;padding:0;width:1200px;height:1200px;overflow:hidden;background:var(--backdrop);}
  .stage{width:1200px;height:1200px;display:flex;align-items:center;justify-content:center;}
  .notecard{width:928px;height:1200px;display:block;}
  .title-city{font-family:"Fredoka",sans-serif;font-weight:600;font-size:50px;fill:var(--title-gold);}
  .title-plan{font-family:"Fredoka",sans-serif;font-weight:600;font-size:46px;fill:var(--ink);}
  .tagline{font-family:"Quicksand",sans-serif;font-weight:700;font-size:31px;fill:var(--teal);}
  .tagline .accent{fill:var(--pink);}
  .survey-text{font-family:"Open Sans",sans-serif;font-weight:700;font-size:24px;fill:var(--white);}
  .survey-text .link{fill:var(--gold);}
  .footer-text{font-family:"Quicksand",sans-serif;font-weight:700;font-size:25px;fill:var(--white);}
  .footer-text .link{fill:var(--gold);}
</style>
</head>
<body>
<main class="stage">
  <svg class="notecard" viewBox="235 83 1028 1330" xmlns="http://www.w3.org/2000/svg">
    <defs>
      <clipPath id="card-clip"><rect x="235" y="83" width="1028" height="1330"/></clipPath>
      <linearGradient id="river-bridge-tone" x1="0" y1="0" x2="0" y2="1">
        <stop offset="0" stop-color="#5f8bc6"/>
        <stop offset="0.45" stop-color="#a9c8e8"/>
        <stop offset="0.55" stop-color="#8d9a8a"/>
        <stop offset="1" stop-color="#6f7a7c"/>
      </linearGradient>
      <linearGradient id="river-valley-tone" x1="0" y1="0" x2="0" y2="1">
        <stop offset="0" stop-color="#5fa3e0"/>
        <stop offset="0.45" stop-color="#3e6a34"/>
        <stop offset="0.65" stop-color="#2f5fa8"/>
        <stop offset="1" stop-color="#1d4a8c"/>
      </linearGradient>
    </defs>

    <g clip-path="url(#card-clip)">
      <rect class="card-paper" x="235" y="83" width="1028" height="1330" fill="var(--paper)"/>

      <!-- corner bars -->
      <g class="corner-bars" fill="var(--teal-light)">
        <rect x="235" y="96" width="180" height="12" rx="6"/>
        <rect x="235" y="128" width="120" height="12" rx="6"/>
      </g>

      <!-- soft background shapes -->
      <g class="halos" fill="var(--halo)">
        <circle cx="470" cy="360" r="190"/>
        <circle cx="960" cy="860" r="205"/>
        <rect x="300" y="140" width="900" height="820" rx="120" opacity="0.55"/>
      </g>

      <!-- flat accent circles -->
      <circle class="ink-disc" cx="470" cy="340" r="150" fill="var(--ink)"/>
      <circle class="gold-disc" cx="920" cy="260" r="105" fill="var(--gold)"/>
      <circle class="teal-disc" cx="960" cy="850" r="170" fill="var(--teal)"/>

      <!-- scattered dots -->
      <g class="dots" fill="var(--teal)">
        <circle cx="1120" cy="150" r="26"/>
        <circle cx="1200" cy="230" r="18"/>
        <circle cx="1140" cy="320" r="14"/>
      </g>
      <circle class="gold-dot" cx="1205" cy="700" r="22" fill="var(--gold)"/>

      <!-- left bars -->
      <g class="ink-bars" fill="var(--ink)">
        <rect x="235" y="880" width="70" height="10" rx="5"/>
        <rect x="235" y="905" width="100" height="10" rx="5"/>
      </g>

      <!-- small round photo -->
      <circle cx="398" cy="787" r="130" fill="var(--paper)"/>
      <circle class="photo-river-valley" cx="398" cy="787" r="120" fill="url(#river-valley-tone)" role="img" aria-label="Photo of a river winding between green wooded bluffs under a blue sky"/>

      <!-- photo frame -->
      <g class="photo-frame">
        <polygon points="750,110 1170,533 750,955 330,533" fill="var(--pink)"/>
        <polygon class="photo-river-bridge" points="750,225 1057,533 750,842 441,533" fill="url(#river-bridge-tone)" role="img" aria-label="Photo of a steel truss railroad bridge crossing a wide river with a sandy shoreline"/>
      </g>

      <!-- bottom-left accent -->
      <rect class="teal-tab" x="215" y="1268" width="95" height="50" rx="25" fill="var(--teal)"/>

      <!-- headings -->
      <text class="title-city" x="757" y="1133" text-anchor="middle">CITY OF FIELDHAVEN</text>
      <text class="title-plan" x="757" y="1185" text-anchor="middle">STRATEGIC PLAN UPDATE</text>
      <text class="tagline" x="757" y="1236" text-anchor="middle">WHAT DO <tspan class="accent">YOU</tspan> WANT FIELDHAVEN TO BE?</text>

      <!-- survey call-to-action -->
      <rect class="survey-pill" x="325" y="1261" width="865" height="65" rx="22" fill="var(--pink)"/>
      <text class="survey-text" x="757" y="1302" text-anchor="middle">Take the Vision Survey at <tspan class="link">http://tnyurl.example/FieldhavenIdeas</tspan></text>

      <!-- footer band -->
      <rect class="footer-band" x="235" y="1353" width="1028" height="60" fill="var(--navy)"/>
      <text class="footer-text" x="757" y="1392" text-anchor="middle">FOR MORE INFO, GO TO : <tspan class="link">WWW.PLAINSFUTUREPLAN.ORG</tspan></text>
    </g>
  </svg>
</main>
</body>
</html>
```